Corvel Lane

Small ageny public transit advocacy, funding and compliance.
Consulting and lobbying efforts for small public transit agencies and communities exploring public transit opportunities.
Updates

I was interested in a simple line sketch suggesting motion, mobility. The card will be black on white. I would like it to include the bUs ones brief; Advocacy, Funding , and Compliance for small transit agencies.

Reason: I have been traveling and have had limited time to respond. Thank you all for your submit talks.

Industry/Entity Type

Consulting

Contact Information for Business Card

Mark D Loyer
Phone (614) 380-2917
Email markdloyer@vantomail.test

```html
<!DOCTYPE html>
<html lang="en">
<head>
<meta charset="utf-8">
<title>Mark D Loyer — Business Card</title>
<link rel="stylesheet" href="https://fonts.googleapis.com/css2?family=Cinzel:wght@400&family=Cormorant+Garamond:wght@400;500&display=swap">
<style>
  :root {
    --paper: #ffffff;
    --ink: #231f20;
    --frame: #1a1a1a;
  }
  * { margin: 0; padding: 0; box-sizing: border-box; }
  html, body {
    width: 1200px;
    height: 999px;
    overflow: hidden;
    background: var(--paper);
  }
  .card {
    position: absolute;
    left: 81px;
    top: 201px;
    width: 1051px;
    height: 601px;
    border: 2px solid var(--frame);
    background: var(--paper);
    color: var(--ink);
  }
  .card__name {
    position: absolute;
    top: 172px;
    left: 0;
    width: 100%;
    text-align: center;
    font-family: "Cinzel", serif;
    font-weight: 400;
    font-size: 48px;
    letter-spacing: 1px;
    line-height: 1;
  }
  .card__services {
    position: absolute;
    top: 443px;
    left: 0;
    width: 100%;
    text-align: center;
    font-family: "Cormorant Garamond", serif;
    font-size: 29px;
    letter-spacing: 6px;
    line-height: 1;
  }
  .card__services .dot {
    display: inline-block;
    width: 6px;
    height: 6px;
    border-radius: 50%;
    background: var(--ink);
    vertical-align: middle;
    margin: 0 6px 0 2px;
    position: relative;
    top: -3px;
  }
  .card__contact {
    position: absolute;
    top: 515px;
    left: 0;
    width: 100%;
    display: flex;
    justify-content: center;
    align-items: center;
    gap: 14px;
    font-family: "Cormorant Garamond", serif;
    font-weight: 500;
    font-size: 28px;
    line-height: 1;
  }
  .contact-item { display: flex; align-items: center; gap: 10px; }
  .contact-icon { width: 24px; height: 24px; flex: none; }
</style>
</head>
<body>
  <div class="card">
    <h1 class="card__name">Mark D Loyer</h1>
    <p class="card__services">ADVOCACY<span class="dot"></span>FUNDING<span class="dot"></span>COMPLIANCE</p>
    <div class="card__contact">
      <span class="contact-item">
        <svg class="contact-icon" viewBox="0 0 24 24" aria-hidden="true">
          <circle cx="12" cy="12" r="12" fill="var(--ink)"/>
          <path d="M8.2 6.2c.5-.3 1.1-.2 1.4.3l1.2 1.9c.3.5.2 1-.2 1.4l-.8.7c.6 1.4 1.7 2.6 3.1 3.3l.7-.8c.4-.4 1-.5 1.4-.2l1.9 1.2c.5.3.6 1 .3 1.4l-.8 1.1c-.5.7-1.4 1-2.2.7-3.4-1.2-6-3.9-7.1-7.3-.3-.8 0-1.7.7-2.2z" fill="var(--paper)"/>
        </svg>
        (614) 380-2917
      </span>
      <span class="contact-item">
        <svg class="contact-icon" viewBox="0 0 24 24" aria-hidden="true">
          <circle cx="12" cy="12" r="12" fill="var(--ink)"/>
          <rect x="6.5" y="8" width="11" height="8" rx="1" fill="var(--paper)"/>
          <path d="M6.8 8.4 12 12.5l5.2-4.1M6.8 15.6l3.8-3.4M17.2 15.6l-3.8-3.4" stroke="var(--ink)" stroke-width="1" fill="none"/>
        </svg>
        markdloyer@vantomail.test
      </span>
    </div>
  </div>
</body>
</html>
```